business card design for a plumbing contractor

i need a double business card for a plumbing business, our initial service is residential Sewer Drain Cleaning.

Target Market(s)

other plumbing Business

Industry/Entity Type

Plumbing

Contact Information for Business Card

www.PipeworksCrestline.example- 5817302946-

Font styles to use
Serif

Colors
ec1f27
0455a3

```html
<!DOCTYPE html>
<html lang="en">
<head>
<meta charset="utf-8">
<title>Pipeworks Crestline – Business Card</title>
<link rel="stylesheet" href="https://fonts.googleapis.com/css2?family=Arimo:wght@400;700&display=swap">
<style>
  :root {
    --stage: #2a2a2a;
    --brand-red: #ec1f27;
    --card-red: #d9312b;
    --brand-blue: #0455a3;
    --paper: #f7f7f7;
    --ink: #222222;
    --logo-grey: #6b6357;
    --white: #ffffff;
  }
  * { margin: 0; padding: 0; box-sizing: border-box; }
  html, body { width: 1200px; height: 997px; overflow: hidden; }
  body {
    background: var(--stage);
    font-family: "Arimo", Arial, sans-serif;
    position: relative;
  }
  .card {
    position: absolute;
    left: 250px;
    width: 700px;
    height: 400px;
    border-radius: 24px;
    overflow: hidden;
  }
  .card-front {
    top: 70px;
    background: var(--card-red);
    display: flex;
    align-items: center;
    justify-content: center;
  }
  .front-name {
    color: var(--white);
    font-weight: 700;
    font-size: 56px;
    line-height: 1;
    letter-spacing: 0.5px;
  }
  .card-back { top: 527px; background: var(--paper); }
  .back-art { position: absolute; inset: 0; }
  .back-name {
    position: absolute;
    left: 150px;
    top: 96px;
    color: var(--logo-grey);
    font-weight: 700;
    font-size: 40px;
    line-height: 1;
  }
  .services {
    position: absolute;
    right: 58px;
    top: 168px;
    text-align: right;
    font-size: 15px;
    line-height: 22px;
    color: var(--ink);
  }
  .person { position: absolute; left: 34px; top: 240px; }
  .person-name { color: var(--brand-red); font-weight: 700; font-size: 22px; }
  .person-role { color: var(--brand-blue); font-weight: 700; font-size: 15px; margin-top: 2px; }
  .contact {
    position: absolute;
    left: 34px;
    top: 300px;
    list-style: none;
    font-size: 16px;
    color: var(--ink);
  }
  .contact li { display: flex; align-items: center; gap: 14px; height: 26px; }
  .contact svg { width: 16px; height: 16px; flex: none; }
  .website {
    position: absolute;
    right: 36px;
    top: 328px;
    color: var(--white);
    font-size: 15px;
    line-height: 18px;
  }
</style>
</head>
<body>
  <section class="card card-front">
    <p class="front-name">Pipeworks Crestline</p>
  </section>

  <section class="card card-back">
    <svg class="back-art" viewBox="0 0 700 400" aria-hidden="true">
      <line x1="548" y1="128" x2="680" y2="128" stroke="var(--brand-blue)" stroke-width="1.2"/>
      <line x1="200" y1="262" x2="600" y2="262" stroke="var(--brand-blue)" stroke-width="1.2"/>
      <path d="M0 366 L322 366 C362 366 366 310 408 310 L408 318 C372 318 370 376 328 376 L0 376 Z" fill="var(--brand-blue)"/>
      <path d="M0 382 L340 382 C384 382 384 318 430 318 L700 318 L700 400 L0 400 Z" fill="var(--card-red)"/>
    </svg>

    <p class="back-name">Pipeworks Crestline</p>

    <div class="services">
      <p>Sewer Drain Cleaning</p>
      <p>Maintenance</p>
      <p>Trenchless Pipe Installs</p>
    </div>

    <div class="person">
      <p class="person-name">Marco Elvidge</p>
      <p class="person-role">Director</p>
    </div>

    <ul class="contact">
      <li>
        <svg viewBox="0 0 16 16" aria-label="Phone"><circle cx="8" cy="8" r="8" fill="var(--brand-blue)"/><path d="M5 4.5h2l.6 2-1 .8a5 5 0 0 0 2.1 2.1l.8-1 2 .6v2c-4 .4-7-2.6-6.5-6.5z" fill="var(--white)"/></svg>
        <span>5817302946</span>
      </li>
      <li>
        <svg viewBox="0 0 16 16" aria-label="Email"><circle cx="8" cy="8" r="8" fill="var(--brand-blue)"/><rect x="4" y="5.5" width="8" height="5.5" fill="var(--white)"/><path d="M4 5.5l4 3 4-3" fill="none" stroke="var(--brand-blue)" stroke-width="0.9"/></svg>
        <span>Dispatch@PipeworksCrestline.example</span>
      </li>
    </ul>

    <p class="website">www.PipeworksCrestline.example</p>
  </section>
</body>
</html>
```